BRIGHTFOLD, Music and Science festival, needs a poster for 2018

BRIGHTFOLD Leiden is a festival that bridges classical music and science in the Leiden Bio Marrow Grounds (The Netherlands). We celebrate our second edition on the 5 & 6 October 2018. This unique cultural product is a collaboration of bio tech companies and Kestrel Academy to deliver an original programme where science is the entry point to discover classical music on futuristic locations.

We want a poster to reflect on the duality science-music. This poster will be used in print and also as the branding foundation for other materials (web, social media, flyers, programmes, etc)

The poster has to use this image:

https://www.filequay.example/s/q2tr7wpx41kd/pixharbor_463028517.jpg?dl=0
https://www.filequay.example/s/m9vc3hz82ntu/pixharbor_463028517.eps?dl=0

We attach the poster from last year, just as a reference, and also the logo

Target Market(s)

Educated adults 25-70 yo

Industry/Entity Type

Festival

Font styles to use
Serif
Sans Serif

Colors

Designer to choose colors to be used in the design.

Requirements
Must have
• Vertical
• Graphic material that we can use for web design, social media, brouchure...
Nice to have
• Impactful image, music and science are stimulating for the brain

```html
<!DOCTYPE html>
<html lang="nl">
<head>
<meta charset="utf-8">
<title>BRIGHTFOLD Leiden – Klassieke Muziek</title>
<link rel="stylesheet" href="https://fonts.googleapis.com/css2?family=Rubik:ital,wght@0,400;0,500;0,700;1,700&display=swap">
<style>
  :root {
    --red-top: #c3283a;
    --wine-mid: #8d2147;
    --plum-low: #5a2456;
    --indigo-base: #352463;
    --glow-amber: rgba(255, 170, 90, 0.55);
    --glow-rose: rgba(255, 95, 110, 0.35);
    --ink: #ffffff;
    --rule: rgba(255, 255, 255, 0.9);
  }
  * { margin: 0; padding: 0; box-sizing: border-box; }
  html, body { width: 778px; height: 1200px; overflow: hidden; }
  body { font-family: "Rubik", Arial, sans-serif; color: var(--ink); }

  .poster {
    position: relative;
    width: 778px;
    height: 1200px;
    overflow: hidden;
    background: linear-gradient(165deg, var(--red-top) 0%, var(--wine-mid) 40%, var(--plum-low) 68%, var(--indigo-base) 100%);
  }

  .festival-header { position: absolute; left: 62px; top: 36px; }
  .festival-title {
    font-weight: 700;
    font-size: 46px;
    line-height: 1;
    letter-spacing: 0.2px;
  }
  .festival-title .brand { font-style: italic; }
  .festival-genre {
    margin-top: 12px;
    font-size: 25px;
    font-weight: 400;
  }

  .wave-artwork {
    position: absolute;
    left: 0;
    top: 150px;
    width: 778px;
    height: 640px;
    background:
      radial-gradient(ellipse 60% 22% at 55% 48%, var(--glow-amber), transparent 70%),
      radial-gradient(ellipse 70% 35% at 40% 58%, var(--glow-rose), transparent 75%);
  }

  .event-details { position: absolute; left: 62px; top: 830px; }
  .rule {
    width: 68px;
    height: 4px;
    background: var(--rule);
  }
  .event-date {
    margin-top: 40px;
    font-weight: 700;
    font-size: 39px;
    line-height: 1;
  }
  .event-venue {
    margin-top: 22px;
    font-size: 29px;
    line-height: 1.4;
    font-weight: 400;
  }
  .event-details .rule.closing { margin-top: 30px; }
  .event-web {
    margin-top: 40px;
    font-size: 20px;
    font-weight: 400;
  }
</style>
</head>
<body>
  <main class="poster">
    <header class="festival-header">
      <h1 class="festival-title"><span class="brand">BRIGHTFOLD</span> Leiden</h1>
      <p class="festival-genre">Klassieke Muziek</p>
    </header>

    <div class="wave-artwork" role="img" aria-label="Glowing flowing wave lines in amber and rose, woven through a network of connected points"></div>

    <section class="event-details">
      <div class="rule"></div>
      <p class="event-date">October 5 - 6, 2018</p>
      <p class="event-venue">Leiden Bio Marrow Grounds,<br>The Netherlands</p>
      <div class="rule closing"></div>
      <p class="event-web">http://www.brightfoldleiden.example</p>
    </section>
  </main>
</body>
</html>
```